Washing powder bag design.

Project Description – Graphic Design Proposal for ORNE Laundry Powder Packaging
We have already explored initial design ideas internally, supported by AI-assisted tools (ChatGPT) to develop early concepts, layouts, and mockups. To support this, we have attached the bag die-cut, where graphics and text are placed as a visual guideline for the intended structure. In addition, we have included a mockup of the product series currently under development to clearly communicate the desired style, direction, and overall visual identity.
The mockup should be regarded as the design foundation for this project and as a starting point for professional refinement.
Scope of Work
We would like you to create three graphic design variants, each based on a different color direction:
1. Variant 1: In line with our current color scheme
2. Variant 2: A blue version
3. Variant 3: A green version
Design Elements to Be Preserved
The following elements must be maintained across all three variants:
• The overall style and visual expression of the mockup
• The leaf-shaped element in the bottom right corner
• The ORNE layout, including typography, positioning, and general look & feel
Summary
While the color palette may vary, the structure, style, and key design elements must remain consistent and be directly based on the attached mockup.
We look forward to seeing your creative interpretation and professional input.
Updates
We need the design to be created based on the attached die-cut file “Orne 10 kg BAG 202526”, including all text elements.
We would like the final to include both the designed die-cut file and a mockup.

```html
<!DOCTYPE html>
<html lang="da">
<head>
<meta charset="utf-8">
<title>ORNE Vaskepulver – die-cut 10 kg</title>
<link href="https://fonts.googleapis.com/css2?family=Outfit:wght@400;500;600;700;800&family=Open+Sans:wght@400;600;700&display=swap" rel="stylesheet">
<style>
:root{
  --green-dark:#2f5a44;
  --green-leaf:#d5e3bd;
  --cream:#f8efdc;
  --cream-light:#faf4e6;
  --paper:#ffffff;
  --band:#cfcfd1;
  --guide-purple:#9a8cc4;
  --guide-green:#7fc49a;
  --hazard:#d8302b;
  --ink:#1e1e1e;
  --page:#ffffff;
}
*{box-sizing:border-box;margin:0;padding:0}
html,body{width:761px;height:1200px;overflow:hidden;background:var(--page)}
body{position:relative;font-family:"Open Sans",sans-serif;color:var(--ink)}
.sheet-title{position:absolute;top:238px;left:0;width:761px;text-align:center;
  font-family:"Outfit",sans-serif;font-weight:700;font-size:29px;letter-spacing:1px;color:var(--green-dark)}
.diecut{position:absolute;left:0;top:290px;width:761px;height:628px;background:var(--cream);overflow:hidden}
.band-h{position:absolute;left:0;width:761px;height:4px;background:var(--band)}
.band-v{position:absolute;top:0;height:628px;width:4px;background:var(--band)}
.trim-line{position:absolute;left:0;width:761px;height:1px;background:#b9b6ae}
.guide{position:absolute;top:0;height:628px;border-left:1px dashed var(--guide-purple);opacity:.8}
.guide.fold{border-left:1px dashed var(--guide-green)}
.punch{position:absolute;width:27px;height:27px;border-radius:50%;background:var(--paper);border:1px solid #777;
  display:flex;align-items:center;justify-content:center;font-size:9px;color:#555;line-height:1}
.mark{position:absolute;font-size:4px;color:#999;letter-spacing:.3px}

/* warning label */
.warning{position:absolute;left:26px;top:106px;width:134px;height:208px;background:var(--paper)}
.warning-title{position:absolute;top:12px;width:100%;text-align:center;font-weight:700;font-size:5.5px;line-height:7px}
.ghs{position:absolute;left:42px;top:38px;width:52px;height:52px}
.warning-text{position:absolute;left:9px;top:106px;width:122px;font-size:3.1px;line-height:3.9px}
.ufi{position:absolute;left:9px;top:201px;font-size:3px}

/* dosage */
.dosage-title{position:absolute;left:26px;top:328px;width:134px;text-align:center;font-family:"Outfit",sans-serif;
  font-weight:600;font-size:12px;line-height:12.5px;color:var(--green-dark)}
.dosage-table{position:absolute;left:36px;top:362px;width:115px;border-collapse:collapse;font-family:"Outfit",sans-serif;color:var(--green-dark)}
.dosage-table td,.dosage-table th{border:0.6px solid var(--green-dark);text-align:center;font-weight:500}
.dosage-table th{font-size:5.5px;line-height:5.5px;height:13px}
.dosage-table td{font-size:5.2px;line-height:6px}
.dosage-table .size{font-size:9px;font-weight:600;width:36px}
.dosage-table tr.r1 td{height:25px}
.dosage-table tr.r2 td{height:24px}
.dosage-table tr.r3 td{height:26px}
.dosage-table tr.foot td{height:10px;font-size:5.5px}
.icon-row{position:absolute;display:flex}
.icon{background:var(--green-dark);color:var(--cream);display:flex;align-items:center;justify-content:center;
  font-family:"Outfit",sans-serif;font-weight:600}
.icon .inner{border:1.4px solid var(--cream);border-radius:4px;display:flex;align-items:center;justify-content:center}
.icon-row.side{left:37px;top:466px;gap:11px}
.icon-row.side .icon{width:29px;height:28px;border-radius:6px}
.icon-row.side .inner{width:22px;height:21px;font-size:9px}
.temps{position:absolute;font-family:"Outfit",sans-serif;font-weight:500;color:var(--green-dark);white-space:nowrap}
.temps.side{left:37px;top:498px;font-size:8px}

/* front */
.brand-name{position:absolute;left:270px;top:196px;width:228px;text-align:center;font-family:"Outfit",sans-serif;
  font-weight:700;font-size:46px;line-height:50px;letter-spacing:1px;color:var(--green-dark)}
.product{position:absolute;left:250px;width:268px;text-align:center;font-family:"Outfit",sans-serif;color:var(--green-dark)}
.product.main{top:310px;font-size:28px;font-weight:700;letter-spacing:.5px}
.product.sub{top:339px;font-size:15.5px;font-weight:600;letter-spacing:.4px}
.product.claim{top:371px;font-size:14.5px;font-weight:500;line-height:17px;letter-spacing:.4px}
.icon-row.front{left:281px;top:437px;gap:6px;align-items:center}
.icon-row.front .icon{width:37px;height:37px;border-radius:8px}
.icon-row.front .inner{width:28px;height:28px;font-size:11px}
.net{font-family:"Outfit",sans-serif;font-weight:500;font-size:17px;color:var(--green-dark);margin-left:6px}
.temps.front{left:281px;top:478px;font-size:10.5px}
.leaf-art{position:absolute;left:440px;top:373px;width:76px;height:156px;z-index:0;
  border-radius:60% 40% 50% 50% / 40% 50% 50% 60%;
  background:linear-gradient(160deg,var(--green-leaf),rgba(213,227,189,.35));opacity:.85}
.icon-row.front,.temps.front{z-index:1}

/* producer */
.producer{position:absolute;left:524px;top:388px;width:82px;height:128px;background:var(--cream-light);
  text-align:center;font-family:"Outfit",sans-serif;color:var(--green-dark)}
.producer .made{margin-top:14px;font-size:5.5px}
.producer .company{margin-top:6px;font-size:10.5px;font-weight:700;white-space:nowrap}
.producer .addr{margin-top:6px;font-size:5.4px;line-height:6.6px}
.producer .eco{margin-top:4px;display:flex;justify-content:center;gap:8px}
.producer .weight{font-size:8.5px;font-weight:600;margin-top:1px}
.producer .t{font-size:3.4px}

/* instructions */
.instructions{position:absolute;left:611px;top:124px;width:130px;height:389px;background:var(--paper);
  border:0.8px solid var(--green-dark);padding:7px 5px;font-size:3.2px;line-height:3.95px;overflow:hidden}
.instructions p{margin-bottom:3px}
.instructions b{font-weight:700}
</style>
</head>
<body>

<h1 class="sheet-title">DIE-CUT FILE ORNE</h1>

<section class="diecut" aria-label="ORNE vaskepulver 10 kg, udfoldet posetryk">
  <div class="band-h" style="top:13px"></div>
  <div class="band-h" style="top:89px"></div>
  <div class="trim-line" style="top:531px"></div>
  <div class="band-h" style="top:616px"></div>
  <div class="band-v" style="left:22px"></div>
  <div class="band-v" style="left:741px"></div>

  <div class="guide" style="left:161px"></div>
  <div class="guide fold" style="left:204px"></div>
  <div class="guide" style="left:248px"></div>
  <div class="guide" style="left:523px"></div>
  <div class="guide fold" style="left:559px"></div>
  <div class="guide" style="left:606px"></div>

  <span class="mark" style="left:730px;top:10px">ZGRZEW</span>
  <span class="mark" style="left:730px;top:86px">ZGRZEW</span>
  <span class="mark" style="left:712px;top:619px">ZGRZEW</span>

  <div class="punch" style="left:11px;top:37px"></div>
  <div class="punch" style="left:60px;top:37px"></div>
  <div class="punch" style="left:321px;top:37px">+</div>
  <div class="punch" style="left:369px;top:37px">+</div>
  <div class="punch" style="left:418px;top:37px"></div>
  <div class="punch" style="left:679px;top:37px"></div>
  <div class="punch" style="left:728px;top:37px"></div>

  <!-- hazard label -->
  <div class="warning">
    <div class="warning-title">Advarsel<br>Warning</div>
    <svg class="ghs" viewBox="0 0 52 52" aria-label="Faresymbol, udråbstegn">
      <rect x="10" y="10" width="32" height="32" transform="rotate(45 26 26)" fill="#fff" stroke="var(--hazard)" stroke-width="3"/>
      <rect x="24" y="14" width="4" height="16" rx="2" fill="#111"/>
      <circle cx="26" cy="35" r="2.6" fill="#111"/>
    </svg>
    <div class="warning-text">
      <b>(DK)</b>Forårsager hudirritation. Forårsager alvorlig øjenirritation.<br>
      Indeholder subtilisin, amylase, alpha, parfume. Kan udløse allergisk reaktion.<br>
      Sikkerhedsdatablad kan på anmodning rekvireres.<br>
      Hvis der er brug for lægehjælp, medbring da beholderen eller etiketten.<br>
      Opbevares utilgængeligt for børn. Vask hænder grundigt efter brug.<br>
      Bær øjenbeskyttelse/ansigtsbeskyttelse/beskyttelseshandsker.<br>
      VED KONTAKT MED ØJNENE: Skyl forsigtigt med vand i flere minutter. Fjern eventuelle kontaktlinser, hvis dette kan gøres let. Fortsæt skylning.<br>
      Ved vedvarende øjenirritation: Søg lægehjælp.<br>
      <b>(GB)</b> Causes skin irritation. Causes serious eye irritation.<br>
      Contains subtilisin, Amylase, Parfume. May produce an allergic reaction.<br>
      Safety data sheet available on request.<br>
      If medical advice is needed, have product container or label at hand.<br>
      Keep out of reach of children. Wash hands thoroughly after handling.<br>
      Wear eye protection/face protection/protective gloves.<br>
      IF IN EYES: Rinse cautiously with water for several minutes.<br>
      Remove contact lenses, if present and easy to do.<br>
      Continue rinsing. If eye irritation persists: Get medical advice/ attention.
    </div>
    <div class="ufi">UFI: A10B-C20D-E30F-G40H</div>
  </div>

  <!-- dosage -->
  <div class="dosage-title">DOSERING<br>• DOSAGE</div>
  <table class="dosage-table">
    <tr><th></th><th>blød -<br>soft</th><th>medium</th><th>hård<br>- hard</th></tr>
    <tr class="r1"><td class="size">1 Kg</td><td>37 ml<br>= 41 g</td><td>37 ml<br>= 61 g</td><td>83 g</td></tr>
    <tr class="r2"><td class="size">5 Kg</td><td>75 Kg</td><td>75 ml<br>= 83 g</td><td>83 g</td></tr>
    <tr class="r3"><td class="size">10 Kg</td><td>112 Kg</td><td>112 ml<br>= 124 g</td><td>144 g</td></tr>
    <tr class="foot"><td colspan="4">75 ml = 83 g</td></tr>
  </table>
  <div class="icon-row side">
    <div class="icon"><div class="inner">120</div></div>
    <div class="icon"><div class="inner">
      <svg width="14" height="15" viewBox="0 0 14 15" aria-label="Vaskemaskine"><rect x="1" y="1" width="12" height="13" rx="1.5" fill="none" stroke="var(--cream)" stroke-width="1.3"/><circle cx="7" cy="8.5" r="3.4" fill="none" stroke="var(--cream)" stroke-width="1.3"/><circle cx="7" cy="8.5" r="1.6" fill="var(--cream)"/></svg>
    </div></div>
    <div class="icon"><div class="inner">
      <svg width="15" height="13" viewBox="0 0 15 13" aria-label="Håndvask"><path d="M1 5h13l-1.5 7h-10z" fill="none" stroke="var(--cream)" stroke-width="1.2"/><path d="M5 6V2.2a1 1 0 0 1 2 0V5M7 5V1.5a1 1 0 0 1 2 0V6" fill="none" stroke="var(--cream)" stroke-width="1"/></svg>
    </div></div>
  </div>
  <div class="temps side">20°C | 30°C | 40°C | 60°C | 90°C</div>

  <!-- front -->
  <div class="brand-name">ORNE</div>
  <div class="product main">VASKEPULVER</div>
  <div class="product sub">LAUNDRY DETERGENT</div>
  <div class="product claim">LIV OG BALANCE<br>I HVERDAGEN</div>
  <div class="leaf-art" role="img" aria-label="Lys grøn bladgren som dekoration i nederste højre hjørne"></div>
  <div class="icon-row front">
    <div class="icon"><div class="inner">120</div></div>
    <div class="icon"><div class="inner">
      <svg width="18" height="19" viewBox="0 0 14 15" aria-label="Vaskemaskine"><rect x="1" y="1" width="12" height="13" rx="1.5" fill="none" stroke="var(--cream)" stroke-width="1.3"/><circle cx="7" cy="8.5" r="3.4" fill="none" stroke="var(--cream)" stroke-width="1.3"/><circle cx="7" cy="8.5" r="1.6" fill="var(--cream)"/></svg>
    </div></div>
    <div class="icon"><div class="inner">
      <svg width="19" height="16" viewBox="0 0 15 13" aria-label="Håndvask"><path d="M1 5h13l-1.5 7h-10z" fill="none" stroke="var(--cream)" stroke-width="1.2"/><path d="M5 6V2.2a1 1 0 0 1 2 0V5M7 5V1.5a1 1 0 0 1 2 0V6" fill="none" stroke="var(--cream)" stroke-width="1"/></svg>
    </div></div>
    <span class="net">10 kg</span>
  </div>
  <div class="temps front">20°C | 30°C | 40°C | 60°C | 90°C</div>

  <!-- producer -->
  <div class="producer">
    <div class="made">Produceret i EU for</div>
    <div class="company">NORDVASK ApS</div>
    <div class="addr">Birkevej 12<br>4300 Holbæk<br>+45 70001234<br>info@nordvask.dk<br>www.nordvask.dk</div>
    <div class="eco">
      <svg width="11" height="11" viewBox="0 0 12 12" aria-label="Genbrug"><path d="M2 6a4 4 0 0 1 7-2.6M10 6a4 4 0 0 1-7 2.6" fill="none" stroke="var(--green-dark)" stroke-width="1"/><path d="M9.6 1.6v2.2H7.4M2.4 10.4V8.2h2.2" fill="none" stroke="var(--green-dark)" stroke-width="1"/></svg>
      <svg width="11" height="11" viewBox="0 0 12 12" aria-label="Materialemærke"><path d="M6 1.5l4.5 8H1.5z" fill="none" stroke="var(--green-dark)" stroke-width="0.9"/></svg>
    </div>
    <div class="weight">10 kg</div>
    <div class="t">20°C | 30°C | 40°C | 60 °C</div>
  </div>

  <!-- instructions -->
  <div class="instructions">
    <p><b>(DK)</b> BRUGERVEJLEDNING – ORNE VASKEPULVER</p>
    <p>Til universel brug.<br>Egnet til alle typer af vaskemaskiner og alle vaskbare tekstiler.<br>Effektiv fra 20°C til 90°C. Udviklet til både kulørt og hvidt tøj.<br>Fjerner snavs, fedt og lugt og efterlader tekstilerne rene og friske.</p>
    <p>Brugsanvisning:<br>Sorter tøjet efter farve og teksttype. Følg altid vaskeanvisningen i tøjet. Fyld vaskemaskinen korrekt – overfyldning reducerer vaskeevnen. Dosér efter vandhårdhed, mængde og tilsmudsning. Hæld pulveret i doseringsskuffen eller direkte i tromlen (i egnet dosisbeholder).<br>Brug mindre dosering til let snavset vasketøj og blødt vand.</p>
    <p>Anbefalinger:<br>• Undgå overdosis – det beskytter både miljø og maskine.<br>• Ved meget hårdt vand kan ekstra dosering være nødvendig.<br>• Ved vanskelige pletter anbefales forbehandling.<br>• Velegnet til septiktanke ved korrekt dosering.</p>
    <p>Opbevaring:<br>Opbevares tørt og tæt lukket.<br>Beskyt mod fugt. Må ikke udsættes for direkte sollys.<br>Opbevares utilgængeligt for børn.</p>
    <p>Sikkerhed:<br>Forårsager alvorlig øjenirritation og kan forårsage hudirritation.<br>Undgå kontakt med øjne og hud.<br>VED KONTAKT MED ØJNENE: Skyl forsigtigt med vand i flere minutter.<br>Fjern kontaktlinser, hvis det er muligt.<br>VED KONTAKT MED HUDEN: Skyl med vand.<br>Sikkerhedsdatablad kan rekvireres efter anmodning.</p>
    <p>Ingredienser (EF 648/2004):<br>Anioniske tensider, nonioniske tensider, zeolitter, polycarboxylater, enzymer (amylase, protease), optisk hvidt, parfume.</p>
    <p><b>(GB)</b> USER GUIDE – ORNE LAUNDRY DETERGENT POWDER</p>
    <p>Universal detergent.<br>Suitable for all types of washing machines and all washable textiles. Effective from 20°C to 90°C.<br>Designed for both coloured and white laundry.<br>Removes dirt, grease and odours, leaving fabrics clean and fresh.</p>
    <p>Instructions for use:<br>Sort laundry by colour and fabric type. Always follow the garment care labels. Load the machine correctly – overloading reduces washing performance.<br>Dose according to water hardness, soil level and load size.<br>Add detergent into the dispenser drawer or directly into the drum using a dosing ball. Use a reduced dosage for lightly soiled laundry and soft water.</p>
    <p>Recommendations:<br>• Avoid overdosing – helps protect both the environment and your machine.<br>• For very hard water, additional detergent may be required.<br>• For stubborn stains, pre-treatment is recommended.<br>• Suitable for septic tanks when used as directed.</p>
    <p>Storage:<br>Store in a dry place with the bag tightly closed.<br>Protect from moisture. Do not expose to direct sunlight.<br>Keep out of reach of children.</p>
    <p>Safety:<br>Causes serious eye irritation and may cause skin irritation.<br>Avoid contact with eyes and skin.<br>IF IN EYES: Rinse cautiously with water for several minutes.<br>Remove contact lenses if possible.<br>IF ON SKIN: Rinse with water.<br>Safety data sheet available on request.</p>
    <p>Ingredients (EC 648/2004):<br>Anionic surfactants, non-ionic surfactants, zeolites, polycarboxylates, enzymes (amylase, protease), optical brightener, perfume.</p>
  </div>
</section>

</body>
</html>
```